New Plumbing Company

We are looking for a smart and creative business card design for our new plumbing company. We are looking for creativity and originality in our business cards.

Industry/Entity Type

Plumbing

Contact Information for Business Card

Kelvora Plumbing
Peter Oswalt
Managing Director
Telephone Number : 0481529046
Email : service@kelvoraplumbing.com.au
Website : www.kelvoraplumbing.com.au
Lic. 318462D

Colors
0692cd
33a6d7
000000

Requirements
Must have
• I want the business card to be designed on a black background using the blue tones i have selected as seen in the company logo.

```html
<!DOCTYPE html>
<html lang="en">
<head>
<meta charset="UTF-8">
<title>Kelvora Plumbing — Business Cards</title>
<link rel="stylesheet" href="https://fonts.googleapis.com/css2?family=Source+Sans+3:wght@400;600&display=swap">
<style>
  :root {
    --backdrop: #2b2622;
    --card: #000000;
    --card-edge: #151515;
    --blue: #0692cd;
    --blue-light: #33a6d7;
    --white: #ffffff;
    --text-soft: #e6e6e6;
    --divider: #1c5f80;
  }
  * { margin: 0; padding: 0; box-sizing: border-box; }
  html, body {
    width: 1200px; height: 900px; overflow: hidden;
    background: var(--backdrop);
    font-family: "Source Sans 3", "Myriad Pro", Arial, sans-serif;
  }
  .canvas {
    position: relative; width: 1200px; height: 900px;
    display: flex; align-items: center; justify-content: center; gap: 40px;
  }
  .card {
    position: relative; width: 540px; height: 308px;
    background: var(--card);
    border: 1px solid var(--card-edge);
    box-shadow: 0 12px 30px rgba(0,0,0,0.45);
    overflow: hidden;
  }

  /* Contact side */
  .card--contact { display: flex; align-items: center; }
  .brand-block {
    width: 215px; height: 100%;
    display: flex; flex-direction: column; align-items: center; justify-content: center; gap: 14px;
  }
  .brand-dot {
    width: 74px; height: 74px; border-radius: 50%;
    border: 6px solid var(--blue);
  }
  .brand-name--stacked {
    color: var(--white); font-weight: 600; font-size: 22px;
    text-align: center; line-height: 1.1;
  }
  .divider {
    width: 1px; height: 200px;
    background: linear-gradient(to bottom, transparent, var(--divider) 20%, var(--divider) 80%, transparent);
  }
  .contact-block { padding-left: 30px; }
  .person-name {
    color: var(--blue); font-weight: 600; font-size: 20px; margin-bottom: 22px;
  }
  .contact-list { list-style: none; }
  .contact-item {
    display: flex; align-items: center; gap: 9px;
    color: var(--text-soft); font-size: 16px; line-height: 23px;
  }
  .contact-icon { width: 11px; height: 11px; fill: var(--blue); flex-shrink: 0; }
  .licence { color: var(--text-soft); font-size: 16px; margin-top: 26px; }

  /* Brand side */
  .card--brand {
    display: flex; flex-direction: column; align-items: center; justify-content: center;
  }
  .brand-row { display: flex; align-items: center; gap: 16px; margin-bottom: 34px; }
  .brand-row .brand-dot { width: 58px; height: 58px; border-width: 5px; }
  .brand-name {
    color: var(--white); font-weight: 400; font-size: 40px; letter-spacing: 0.5px;
  }
  .services { color: var(--white); font-size: 17px; letter-spacing: 0.3px; }
  .tagline { color: var(--blue); font-size: 17px; margin-top: 2px; }
</style>
</head>
<body>
<main class="canvas">

  <section class="card card--contact" aria-label="Business card, contact side">
    <div class="brand-block">
      <span class="brand-dot" aria-hidden="true"></span>
      <span class="brand-name--stacked">Kelvora<br>Plumbing</span>
    </div>
    <div class="divider" aria-hidden="true"></div>
    <div class="contact-block">
      <h2 class="person-name">Peter Oswalt</h2>
      <ul class="contact-list">
        <li class="contact-item">
          <svg class="contact-icon" viewBox="0 0 24 24" aria-hidden="true"><path d="M6.6 10.8a15.1 15.1 0 0 0 6.6 6.6l2.2-2.2c.3-.3.7-.4 1-.2 1.1.4 2.3.6 3.6.6.6 0 1 .4 1 1V20c0 .6-.4 1-1 1C10.6 21 3 13.4 3 4c0-.6.4-1 1-1h3.5c.6 0 1 .4 1 1 0 1.3.2 2.5.6 3.6.1.3 0 .7-.2 1z"/></svg>
          0481 529 046
        </li>
        <li class="contact-item">
          <svg class="contact-icon" viewBox="0 0 24 24" aria-hidden="true"><path d="M2 5h20v14H2z M2 5l10 8 10-8" stroke="#000" stroke-width="1.5"/></svg>
          service@kelvoraplumbing.com.au
        </li>
        <li class="contact-item">
          <svg class="contact-icon" viewBox="0 0 24 24" aria-hidden="true"><circle cx="12" cy="12" r="11"/><path d="M1 12h22M12 1c3 3 4 7 4 11s-1 8-4 11M12 1c-3 3-4 7-4 11s1 8 4 11" stroke="#000" stroke-width="1.6" fill="none"/></svg>
          www.kelvoraplumbing.com.au
        </li>
      </ul>
      <p class="licence">Lic. 318462D</p>
    </div>
  </section>

  <section class="card card--brand" aria-label="Business card, brand side">
    <div class="brand-row">
      <span class="brand-dot" aria-hidden="true"></span>
      <span class="brand-name">Kelvora Plumbing</span>
    </div>
    <p class="services">Plumbing | Drainage | Gas Fitting</p>
    <p class="tagline">24/7 Emergency Service</p>
  </section>

</main>
</body>
</html>
```